we do all sorts of cleaning however bookings are limited!
why not chose the right cleaners for you!
pressure cleaning, window cleaning, office, end of lease clean, accommodation, industrial and commercial cleaning and house cleaning

Logo Text

Bright Nest Cleaning Service

```html
<!DOCTYPE html>
<html lang="en">
<head>
<meta charset="utf-8">
<title>Bright Nest Cleaning Service – Business Cards</title>
<link href="https://fonts.googleapis.com/css2?family=Lato:ital,wght@0,400;0,700;0,900;1,900&display=swap" rel="stylesheet">
<style>
  :root {
    --bg: #3a3a3a;
    --card-dark: #1e1e1f;
    --card-light: #ffffff;
    --brand-blue: #08aeea;
    --brand-green: #8cc63f;
    --text-light: #ffffff;
  }
  * { box-sizing: border-box; margin: 0; padding: 0; }
  html, body { width: 1200px; height: 875px; overflow: hidden; }
  body {
    background: var(--bg);
    font-family: "Lato", Arial, sans-serif;
    position: relative;
  }
  .card {
    position: absolute;
    width: 540px;
    height: 309px;
    border-radius: 18px;
    overflow: hidden;
    box-shadow: 0 18px 40px rgba(0,0,0,.45);
  }
  .card--back { left: 40px; top: 283px; background: var(--card-dark); }
  .card--front { left: 620px; top: 283px; background: var(--card-light); }

  .brand {
    display: flex;
    align-items: center;
    gap: 10px;
    color: var(--brand-blue);
    font-weight: 900;
    line-height: 1.05;
  }
  .brand__dot {
    flex: none;
    border-radius: 50%;
    background: var(--brand-green);
  }
  .card--back .brand {
    position: absolute; left: 0; right: 0; top: 58px;
    justify-content: center;
    font-size: 38px;
  }
  .card--back .brand__dot { width: 22px; height: 22px; }
  .card--back .brand__name small { display: block; font-size: 22px; letter-spacing: 2px; }

  .services {
    position: absolute; left: 30px; right: 30px; top: 190px;
    text-align: center;
    color: var(--text-light);
    font-size: 14.5px;
    line-height: 1.55;
  }
  .services__headline {
    color: var(--brand-blue);
    font-weight: 900;
    font-style: italic;
    font-size: 15px;
    margin-bottom: 4px;
  }
  .services .sep { color: var(--brand-green); font-weight: 900; padding: 0 3px; }

  .wave { position: absolute; inset: 0; width: 100%; height: 100%; }

  .card--front .brand {
    position: absolute; left: 32px; top: 72px;
    font-size: 26px;
  }
  .card--front .brand__dot { width: 16px; height: 16px; }
  .card--front .brand__name small { display: block; font-size: 13px; letter-spacing: 1.5px; }

  .person { position: absolute; left: 34px; top: 172px; }
  .person__name { color: var(--brand-blue); font-weight: 900; font-size: 25px; letter-spacing: 1px; }
  .person__role { color: var(--brand-green); font-size: 15px; margin-top: 2px; }

  .contacts {
    position: absolute; right: 24px; top: 80px;
    list-style: none;
    color: var(--text-light);
    font-size: 12.5px;
    line-height: 1.75;
    text-align: right;
  }
  .contacts li { display: flex; align-items: center; justify-content: flex-end; gap: 8px; }
  .contacts svg { width: 12px; height: 12px; fill: var(--text-light); flex: none; }
  .contacts .address { align-items: flex-start; }
  .contacts .address svg { margin-top: 4px; }
</style>
</head>
<body>

<section class="card card--back">
  <div class="brand">
    <span class="brand__dot"></span>
    <span class="brand__name">Bright Nest<small>CLEANING SERVICE</small></span>
  </div>
  <div class="services">
    <p class="services__headline">WHY NOT CHOSE THE RIGHT CLEANERS FOR YOU!</p>
    <p>Pressure Cleaning <span class="sep">•</span> Window Cleaning <span class="sep">•</span> Office <span class="sep">•</span> End of Lease Clean</p>
    <p>Accommodation <span class="sep">•</span> Industrial &amp; Commercial <span class="sep">•</span> Cleaning &amp; House Cleaning</p>
  </div>
</section>

<section class="card card--front">
  <svg class="wave" viewBox="0 0 540 309" preserveAspectRatio="none" aria-hidden="true">
    <path d="M0 258 C120 250 230 225 290 160 C330 115 345 70 400 45 C440 28 490 22 540 20 L540 309 L0 309 Z" fill="#08aeea"/>
    <path d="M10 250 C130 238 235 210 285 150 C322 104 338 58 392 34 C430 18 470 12 500 12" fill="none" stroke="#8cc63f" stroke-width="4"/>
    <path d="M0 283 C130 272 240 248 296 190" fill="none" stroke="#ffffff" stroke-width="6"/>
  </svg>

  <div class="brand">
    <span class="brand__dot"></span>
    <span class="brand__name">Bright Nest<small>CLEANING SERVICE</small></span>
  </div>

  <div class="person">
    <p class="person__name">DANIEL REYES</p>
    <p class="person__role">Founder &amp; CEO</p>
  </div>

  <ul class="contacts">
    <li>(555) 210-4836
      <svg viewBox="0 0 24 24"><path d="M6.6 10.8a15 15 0 0 0 6.6 6.6l2.2-2.2c.3-.3.7-.4 1-.2 1.1.4 2.3.6 3.6.6.6 0 1 .4 1 1V20c0 .6-.4 1-1 1A17 17 0 0 1 3 4c0-.6.4-1 1-1h3.5c.6 0 1 .4 1 1 0 1.3.2 2.5.6 3.6.1.3 0 .7-.2 1z"/></svg></li>
    <li>(555) 210-4837
      <svg viewBox="0 0 24 24"><path d="M7 1h10a2 2 0 0 1 2 2v18a2 2 0 0 1-2 2H7a2 2 0 0 1-2-2V3a2 2 0 0 1 2-2zm0 3v14h10V4zm5 15.5a1.2 1.2 0 1 0 0 2.4 1.2 1.2 0 0 0 0-2.4z"/></svg></li>
    <li>(555) 210-4838
      <svg viewBox="0 0 24 24"><path d="M6 2h10v6H6zM3 9h18a1 1 0 0 1 1 1v8h-4v4H6v-4H2v-8a1 1 0 0 1 1-1zm5 7v4h8v-4z"/></svg></li>
    <li>info@brightnestclean.com
      <svg viewBox="0 0 24 24"><path d="M2 5h20v14H2zm2 2v.5l8 5 8-5V7zm0 2.8V17h16V9.8l-8 5z"/></svg></li>
    <li>brightnestclean.com
      <svg viewBox="0 0 24 24"><path d="M12 2a10 10 0 1 0 0 20 10 10 0 0 0 0-20zm6.9 9h-3a15 15 0 0 0-1.3-6A8 8 0 0 1 18.9 11zM12 4c.9 1.3 1.7 3.9 1.9 7h-3.8c.2-3.1 1-5.7 1.9-7zM9.4 5a15 15 0 0 0-1.3 6h-3A8 8 0 0 1 9.4 5zM5.1 13h3a15 15 0 0 0 1.3 6A8 8 0 0 1 5.1 13zM12 20c-.9-1.3-1.7-3.9-1.9-7h3.8c-.2 3.1-1 5.7-1.9 7zm2.6-1a15 15 0 0 0 1.3-6h3a8 8 0 0 1-4.3 6z"/></svg></li>
    <li class="address">18 Harbor Lane, Easton<br>NSW 2150, Australia
      <svg viewBox="0 0 24 24"><path d="M12 2a7 7 0 0 0-7 7c0 5 7 13 7 13s7-8 7-13a7 7 0 0 0-7-7zm0 9.5a2.5 2.5 0 1 1 0-5 2.5 2.5 0 0 1 0 5z"/></svg></li>
  </ul>
</section>

</body>
</html>
```